Bref créative
BrindleWorks Stationery
Package
Use same font as used in my logo
Myriad
Professional
Marc T. Delvaux
Founder
418 Quarry Lane
Alderwick, OR 97855
marc.delvaux@brindleworks-mail.com
www.brindleworks-mail.com

```html
<!DOCTYPE html>
<html lang="en">
<head>
<meta charset="utf-8">
<title>BrindleWorks Business Cards</title>
<link rel="stylesheet" href="https://fonts.googleapis.com/css2?family=Source+Sans+3:wght@300;400;600;700&display=swap">
<style>
  :root {
    --stage: #e9e7e3;
    --card-white: #ffffff;
    --card-dark: #2a2a2a;
    --ink: #3a3a3a;
    --ink-soft: #6d6d6d;
    --rule: #cfcfcf;
    --accent-green: #5cb85c;
    --band-dark: #262626;
    --mark-ring: #ffffff;
    --url-grey: #9a9a9a;
  }
  * { box-sizing: border-box; margin: 0; padding: 0; }
  html, body {
    width: 1200px; height: 629px; overflow: hidden;
    background: var(--stage);
    font-family: "Source Sans 3", "Myriad Pro", sans-serif;
    color: var(--ink);
  }
  .stage {
    width: 1200px; height: 629px;
    display: flex; align-items: center; justify-content: center; gap: 50px;
  }
  .card {
    position: relative; width: 525px; height: 300px;
    border-radius: 4px; overflow: hidden;
    box-shadow: 0 6px 18px rgba(0,0,0,.18);
  }

  /* Front */
  .card--front { background: var(--card-white); }
  .brand {
    position: absolute; left: 30px; top: 70px;
    display: flex; align-items: center; gap: 9px;
  }
  .brand__mark {
    width: 40px; height: 40px; border-radius: 50%;
    background: var(--ink); flex: none;
  }
  .brand__name {
    font-size: 32px; font-weight: 400; color: var(--ink);
    letter-spacing: -0.5px; white-space: nowrap;
  }
  .person { position: absolute; left: 79px; top: 120px; }
  .person__name { font-size: 15px; font-weight: 700; color: var(--ink); white-space: nowrap; }
  .person__title { font-size: 12.5px; font-weight: 400; color: var(--ink-soft); margin-top: 1px; }
  .address {
    position: absolute; left: 30px; top: 214px;
    font-size: 11.5px; color: var(--ink-soft); white-space: nowrap;
  }
  .divider {
    position: absolute; left: 288px; top: 64px; width: 1px; height: 108px;
    background: var(--rule);
  }
  .contacts {
    position: absolute; left: 300px; top: 72px;
    list-style: none; display: flex; flex-direction: column; gap: 13px;
  }
  .contact {
    display: flex; align-items: center; gap: 7px;
    font-size: 10.5px; color: var(--ink); white-space: nowrap;
  }
  .contact__icon {
    width: 18px; height: 18px; border-radius: 50%; background: var(--ink);
    display: flex; align-items: center; justify-content: center; flex: none;
  }
  .front-edge { position: absolute; left: 0; bottom: 0; width: 525px; height: 60px; }

  /* Back */
  .card--back { background: var(--card-dark); }
  .back-mark {
    position: absolute; left: 50%; top: 118px; transform: translateX(-50%);
    width: 66px; height: 66px; border-radius: 50%;
    border: 4px solid var(--mark-ring); background: var(--card-dark);
  }
  .back-url {
    position: absolute; left: 34px; bottom: 30px;
    font-size: 11px; letter-spacing: 3px; color: var(--url-grey);
  }
  .back-edge { position: absolute; left: 0; bottom: 0; width: 525px; height: 40px; }
</style>
</head>
<body>
<main class="stage">
  <section class="card card--front" aria-label="Business card front">
    <div class="brand">
      <span class="brand__mark"></span>
      <span class="brand__name">BrindleWorks</span>
    </div>
    <div class="person">
      <p class="person__name">Marc T. Delvaux</p>
      <p class="person__title">Founder</p>
    </div>
    <div class="divider"></div>
    <ul class="contacts">
      <li class="contact">
        <span class="contact__icon">
          <svg width="10" height="10" viewBox="0 0 24 24"><path fill="#fff" d="M6.6 10.8a15.1 15.1 0 0 0 6.6 6.6l2.2-2.2a1 1 0 0 1 1-.25 11.4 11.4 0 0 0 3.6.57 1 1 0 0 1 1 1V20a1 1 0 0 1-1 1A17 17 0 0 1 3 4a1 1 0 0 1 1-1h3.5a1 1 0 0 1 1 1c0 1.25.2 2.45.57 3.57a1 1 0 0 1-.25 1z"/></svg>
        </span>
        541.555.0142
      </li>
      <li class="contact">
        <span class="contact__icon">
          <svg width="10" height="10" viewBox="0 0 24 24"><path fill="#fff" d="M3 5h18v14H3zm2 2v.5l7 4.5 7-4.5V7z"/></svg>
        </span>
        marc.delvaux@brindleworks-mail.com
      </li>
      <li class="contact">
        <span class="contact__icon">
          <svg width="10" height="10" viewBox="0 0 24 24"><circle cx="12" cy="12" r="9" fill="none" stroke="#fff" stroke-width="2"/><path d="M3 12h18M12 3c3 3 3 15 0 18M12 3c-3 3-3 15 0 18" fill="none" stroke="#fff" stroke-width="1.6"/></svg>
        </span>
        www.brindleworks-mail.com
      </li>
    </ul>
    <p class="address">418 Quarry Lane Alderwick, OR 97855</p>
    <svg class="front-edge" viewBox="0 0 525 60" preserveAspectRatio="none">
      <path d="M0 42 Q262 20 525 42 L525 60 L0 60 Z" fill="var(--band-dark)"/>
      <path d="M0 38 Q262 16 525 38" fill="none" stroke="var(--accent-green)" stroke-width="3"/>
    </svg>
  </section>

  <section class="card card--back" aria-label="Business card back">
    <span class="back-mark"></span>
    <p class="back-url">www.brindleworks-mail.com</p>
    <svg class="back-edge" viewBox="0 0 525 40" preserveAspectRatio="none">
      <path d="M0 30 Q262 14 525 30" fill="none" stroke="#3c3c3c" stroke-width="2"/>
    </svg>
  </section>
</main>
</body>
</html>
```